PowerPoint Template for Meridian Liaison Hub. Website is www.meridianliaisonhub.example

The tagline for the Center is "Connecting the brightest minds in healthcare"

```html
<!DOCTYPE html>
<html lang="en">
<head>
<meta charset="utf-8">
<title>Meridian Liaison Hub – Presentation Template</title>
<link rel="stylesheet" href="https://fonts.googleapis.com/css2?family=Montserrat:wght@300;400;500;600;700&display=swap">
<style>
  :root{
    --navy:#1b2f5e;
    --navy-soft:#3a4f7e;
    --grey-text:#6b7280;
    --rule:#c9cdd6;
    --paper:#ffffff;
    --photo-light:#dfe6ef;
    --photo-mid:#b8c6d8;
    --hero-a:#4b6392;
    --hero-b:#8197bd;
  }
  *{box-sizing:border-box;margin:0;padding:0}
  html,body{width:900px;height:1200px;overflow:hidden;background:var(--paper)}
  body{position:relative;font-family:'Montserrat',sans-serif;color:var(--navy)}
  .slide{position:absolute;width:422px;height:238px;background:var(--paper);
    box-shadow:2px 3px 5px rgba(0,0,0,.35);overflow:hidden}
  .col-a{left:12px}.col-b{left:454px}
  .row-1{top:34px}.row-2{top:290px}.row-3{top:547px}.row-4{top:804px}

  .slide-title{position:absolute;left:24px;top:20px;font-size:11px;font-weight:600;letter-spacing:.4px}
  .corner-mark{position:absolute;right:12px;top:16px;display:flex;align-items:center;gap:3px;
    font-size:5px;font-weight:600;color:var(--navy)}
  .corner-mark .dot{width:14px;height:14px;border:1.5px solid var(--navy);border-radius:50%}
  .page-no{position:absolute;left:24px;bottom:6px;width:10px;height:10px;border:1px solid var(--navy-soft);
    border-radius:50%;font-size:4.5px;display:flex;align-items:center;justify-content:center}
  .footer-name{position:absolute;right:26px;bottom:8px;font-size:4px;font-weight:500;text-transform:uppercase;color:var(--navy)}

  .photo{position:absolute;border-radius:50%;overflow:hidden;
    background:radial-gradient(circle at 40% 40%,var(--photo-light),var(--photo-mid))}

  .small-print{font-size:3.6px;line-height:1.35;color:var(--grey-text)}

  /* cover */
  .cover-title{position:absolute;right:20px;top:52px;text-align:right;font-size:10.5px;font-weight:600;line-height:1.25;letter-spacing:.3px}
  .cover-meta{position:absolute;right:20px;top:84px;font-size:4.5px;color:var(--navy-soft)}
  .wordmark{position:absolute;right:22px;bottom:30px;display:flex;align-items:center;gap:4px;
    font-size:8px;font-weight:600;color:var(--navy)}
  .wordmark .dot{width:20px;height:20px;border:2px solid var(--navy);border-radius:50%}

  /* agenda */
  .agenda-rule{position:absolute;left:145px;top:0;bottom:0;width:1px;background:var(--rule)}
  .agenda-list{position:absolute;left:142px;top:66px;list-style:none}
  .agenda-list li{display:flex;align-items:center;gap:6px;height:25px;font-size:6px;color:var(--navy-soft)}
  .agenda-list li::before{content:"";width:5px;height:5px;border-radius:50%;background:var(--navy)}

  /* section */
  .section{background:linear-gradient(110deg,var(--hero-a),var(--hero-b))}
  .section-heading{position:absolute;right:218px;top:64px;text-align:right;color:#fff;font-size:19px;font-weight:300;line-height:1.2}
  .section-lead{position:absolute;right:218px;top:142px;width:140px;text-align:right;color:#fff;font-size:5px;line-height:1.4}
  .section .photo{border:4px solid #fff}
  .section .wordmark{left:14px;right:auto;bottom:14px;color:#fff;font-size:7px}
  .section .wordmark .dot{width:14px;height:14px;border-color:#fff;border-width:1.5px}

  .text-col{position:absolute;left:205px;width:192px;text-align:justify}
  .lead-bold{font-size:5px;font-weight:600;line-height:1.35;color:var(--navy)}
  .body-copy{font-size:4.2px;line-height:1.4;color:var(--grey-text);margin-top:7px}

  .feature-lead{position:absolute;left:205px;top:68px;width:200px;text-align:center;font-size:6.3px;font-weight:500;line-height:1.35}
  .feature-grid{position:absolute;left:210px;top:116px;display:grid;grid-template-columns:100px 100px;row-gap:14px}
  .feature{display:flex;gap:7px}
  .feature svg{width:14px;height:14px;flex:none;margin-top:4px}
  .feature h4{font-size:4.2px;font-weight:600;margin-bottom:2px}

  .intro{position:absolute;left:24px;top:36px;width:366px;font-size:5px;line-height:1.35;color:var(--grey-text)}
  .timeline{position:absolute;left:82px;top:122px;width:257px;height:1px;background:var(--rule)}
  .milestone{position:absolute;top:94px;width:76px;margin-left:-38px;text-align:center}
  .milestone svg{width:14px;height:16px;display:block;margin:0 auto 8px}
  .milestone .node{width:5px;height:5px;border-radius:50%;background:var(--navy);margin:0 auto 6px}
  .milestone h4{font-size:5.5px;font-weight:400;color:var(--navy-soft);line-height:1.2;margin-bottom:4px}

  .network{position:absolute;left:48px;top:64px;width:196px;height:136px;border-radius:8px;
    background:radial-gradient(circle at 50% 30%,var(--navy-soft),#e7ebf2 70%)}
  .network-text{position:absolute;right:48px;top:106px;width:130px;text-align:right}
  .network-text h3{font-size:11px;font-weight:600;margin-bottom:4px}
  .network-text p{font-size:4.8px;line-height:1.35;color:var(--grey-text)}

  .steps{position:absolute;left:50px;top:88px;width:150px}
  .steps::before{content:"";position:absolute;left:2px;top:4px;height:88px;width:1px;background:var(--rule)}
  .step{position:relative;padding-left:9px;height:44px}
  .step::before{content:"";position:absolute;left:0;top:2px;width:5px;height:5px;border-radius:50%;background:var(--navy)}
  .step h4{font-size:5.5px;font-weight:400;color:var(--navy-soft);margin-bottom:3px}
</style>
</head>
<body>

<!-- Slide 1: cover -->
<section class="slide col-a row-1">
  <div class="photo" role="img" aria-label="Photo of a doctor holding a patient's hand" style="left:16px;top:8px;width:220px;height:220px"></div>
  <h1 class="cover-title">CONNECTING THE BRIGHTEST<br>MINDS IN HEALTHCARE</h1>
  <p class="cover-meta">LOREM IPSUM DOLOR &nbsp;|&nbsp; 01.01.2018</p>
  <div class="wordmark"><span class="dot"></span>Meridian Liaison Hub</div>
</section>

<!-- Slide 2: agenda -->
<section class="slide col-b row-1">
  <h2 class="slide-title">LOREM IPSUM</h2>
  <div class="corner-mark"><span class="dot"></span>Meridian Liaison Hub</div>
  <div class="agenda-rule"></div>
  <ul class="agenda-list">
    <li>Lorem Ipsum Dolor Sit Amet</li>
    <li>Lorem Ipsum Dolor Sit Amet</li>
    <li>Lorem Ipsum Dolor Sit Amet</li>
    <li>Lorem Ipsum Dolor Sit Amet</li>
    <li>Lorem Ipsum Dolor Sit Amet</li>
    <li>Lorem Ipsum Dolor Sit Amet</li>
  </ul>
  <span class="page-no">2</span>
  <span class="footer-name">Meridian Liaison Hub</span>
</section>

<!-- Slide 3: section divider -->
<section class="slide col-a row-2 section" role="img" aria-label="Blue-toned photo of a clinician with a stethoscope">
  <h2 class="section-heading">Lorem Ipsum<br>Dolor Sit<br>Amet</h2>
  <p class="section-lead">Lorem ipsum dolor sit amet, consetetur sadipscing elitr, sed diam nonumy eirmod tempor invidunt ut labore et dolore magna.</p>
  <div class="photo" role="img" aria-label="Photo of hands holding a stethoscope" style="left:236px;top:39px;width:160px;height:160px"></div>
  <div class="wordmark"><span class="dot"></span>Meridian Liaison Hub</div>
</section>

<!-- Slide 4: text and photo -->
<section class="slide col-b row-2">
  <h2 class="slide-title">LOREM IPSUM</h2>
  <div class="corner-mark"><span class="dot"></span>Meridian Liaison Hub</div>
  <div class="photo" role="img" aria-label="Photo of a doctor writing on a clipboard at a desk" style="left:32px;top:42px;width:160px;height:160px"></div>
  <div class="text-col" style="top:50px">
    <p class="lead-bold">Lorem ipsum dolor sit amet, consetetur sadipscing elitr, sed diam nonumy eirmod tempor invidunt ut labore et dolore magna aliquyam erat, sed diam voluptua. At vero eos et accusam et justo duo dolores et ea rebum.</p>
    <p class="body-copy">At vero eos et accusam et justo duo dolores et ea rebum. Stet clita kasd gubergren, no sea takimata sanctus est Lorem ipsum dolor sit amet. Lorem ipsum dolor sit amet, consetetur sadipscing elitr, sed diam nonumy eirmod tempor invidunt ut labore et dolore magna aliquyam erat, sed diam voluptua. At vero eos et accusam et justo duo dolores et ea rebum. Stet clita kasd gubergren, no sea takimata sanctus est Lorem ipsum dolor sit amet.</p>
    <p class="body-copy">Stet clita kasd gubergren, no sea takimata sanctus est Lorem ipsum dolor sit amet. Lorem ipsum dolor sit amet, consetetur sadipscing elitr, sed diam nonumy eirmod tempor invidunt ut labore et dolore magna aliquyam erat, sed diam voluptua. At vero eos et accusam et justo duo dolores et ea rebum. Stet clita kasd gubergren, no sea takimata sanctus est Lorem ipsum dolor sit amet. Lorem ipsum dolor sit amet, consetetur sadipscing elitr, sed diam nonumy eirmod tempor invidunt ut labore et dolore magna aliquyam erat, sed diam voluptua. At vero eos et accusam et justo duo dolores et ea rebum. Duis autem vel eum iriure dolor in hendrerit in vulputate velit esse molestie consequat, vel illum dolore eu feugiat nulla facilisis at vero eros et accumsan et iusto odio dignissim qui blandit praesent luptatum zzril.</p>
  </div>
  <span class="page-no">4</span>
  <span class="footer-name">Meridian Liaison Hub</span>
</section>

<!-- Slide 5: features -->
<section class="slide col-a row-3">
  <h2 class="slide-title">LOREM IPSUM</h2>
  <div class="corner-mark"><span class="dot"></span>Meridian Liaison Hub</div>
  <div class="photo" role="img" aria-label="Photo of a smiling nurse giving a thumbs up" style="left:32px;top:43px;width:160px;height:160px"></div>
  <p class="feature-lead">Lorem ipsum dolor sit amet, consetetur sadipscing elitr, sed diam nonumy eirmod tempor invidunt ut labore et dolore magna aliquyam erat, sed diam voluptua. At vero eos et accusam et justo duo dolores et ea rebum.</p>
  <div class="feature-grid">
    <div class="feature">
      <svg viewBox="0 0 14 14" fill="none" stroke="#1b2f5e" stroke-width="1"><rect x="1.5" y="5" width="11" height="4" rx="2" transform="rotate(35 7 7)"/></svg>
      <div><h4>Lorem ipsum</h4><p class="small-print">In enim justo, rhoncus ut, imperdiet a, venenatis vitae, justo. Nullam dictum felis eu pede.</p></div>
    </div>
    <div class="feature">
      <svg viewBox="0 0 14 14" fill="none" stroke="#1b2f5e" stroke-width="1"><path d="M2 6h10a5 5 0 0 1-10 0zM7 11v2M4 13h6"/></svg>
      <div><h4>Lorem ipsum</h4><p class="small-print">In enim justo, rhoncus ut, imperdiet a, venenatis vitae, justo. Nullam dictum felis eu pede.</p></div>
    </div>
    <div class="feature">
      <svg viewBox="0 0 14 14" fill="none" stroke="#1b2f5e" stroke-width="1"><circle cx="7" cy="7" r="5"/><path d="M7 4v6M4 7h6"/></svg>
      <div><h4>Lorem ipsum</h4><p class="small-print">In enim justo, rhoncus ut, imperdiet a, venenatis vitae, justo. Nullam dictum felis eu pede.</p></div>
    </div>
    <div class="feature">
      <svg viewBox="0 0 14 14" fill="none" stroke="#1b2f5e" stroke-width="1"><rect x="2.5" y="2" width="9" height="11" rx="1"/><path d="M4 9h2l1-3 1 4 1-1h1"/></svg>
      <div><h4>Lorem ipsum</h4><p class="small-print">In enim justo, rhoncus ut, imperdiet a, venenatis vitae, justo. Nullam dictum felis eu pede.</p></div>
    </div>
  </div>
  <span class="page-no">6</span>
  <span class="footer-name">Meridian Liaison Hub</span>
</section>

<!-- Slide 6: timeline -->
<section class="slide col-b row-3">
  <h2 class="slide-title">LOREM IPSUM</h2>
  <div class="corner-mark"><span class="dot"></span>Meridian Liaison Hub</div>
  <p class="intro">Lorem ipsum dolor sit amet, consetetur sadipscing elitr, sed diam nonumy eirmod tempor invidunt ut labore et dolore magna aliquyam erat, sed diam voluptua. At vero eos et accusam et justo duo dolores et ea rebum. Stet clita kasd gubergren, no sea takimata sanctus est Lorem ipsum dolor sit amet. Lorem ipsum dolor sit amet, consetetur sadipscing elitr, sed diam.</p>
  <div class="timeline"></div>
  <div class="milestone" style="left:82px">
    <svg viewBox="0 0 14 16" fill="none" stroke="#1b2f5e" stroke-width="1"><rect x="2" y="1" width="10" height="14"/><path d="M5 5h4M5 8h4M5 11h4"/></svg>
    <div class="node"></div>
    <h4>Lorem ipsum<br>dolor sit amet</h4>
    <p class="small-print">In enim justo, rhoncus ut, imperdiet a, venenatis vitae, justo. Nullam dictum felis eu pede.</p>
  </div>
  <div class="milestone" style="left:211px">
    <svg viewBox="0 0 14 16" fill="none" stroke="#1b2f5e" stroke-width="1"><path d="M7 1v14M2 5c3-2 7-2 10 0M4 9c2 1 4 1 6 0"/></svg>
    <div class="node"></div>
    <h4>Lorem ipsum<br>dolor sit amet</h4>
    <p class="small-print">In enim justo, rhoncus ut, imperdiet a, venenatis vitae, justo. Nullam dictum felis eu pede.</p>
  </div>
  <div class="milestone" style="left:339px">
    <svg viewBox="0 0 14 16" fill="none" stroke="#1b2f5e" stroke-width="1"><path d="M5 2h3v7H5zM3 13h9M6 9v4M9 11a3 3 0 0 0 0-5"/></svg>
    <div class="node"></div>
    <h4>Lorem ipsum<br>dolor sit amet</h4>
    <p class="small-print">In enim justo, rhoncus ut, imperdiet a, venenatis vitae, justo. Nullam dictum felis eu pede.</p>
  </div>
  <span class="page-no">7</span>
  <span class="footer-name">Meridian Liaison Hub</span>
</section>

<!-- Slide 7: network -->
<section class="slide col-a row-4">
  <div class="corner-mark"><span class="dot"></span>Meridian Liaison Hub</div>
  <div class="network" role="img" aria-label="Illustration of a cloud linked to medical icons in a network"></div>
  <div class="network-text">
    <h3>LOREM IPSUM</h3>
    <p>Lorem ipsum dolor sit amet, consetetur sadipscing elitr, sed diam nonumy eirmod tempor invidunt ut labore et dolore magna aliquyam erat, sed diam voluptua. At vero eos et accusam et justo duo dolores et ea rebum. Stet clita kasd gubergren, no sea takimata sanctus est Lorem ipsum dolor sit amet. Lorem ipsum dolor sit amet, consetetur sadipscing elitr, sed diam.</p>
  </div>
  <span class="page-no">8</span>
  <span class="footer-name">Meridian Liaison Hub</span>
</section>

<!-- Slide 8: steps and photo -->
<section class="slide col-b row-4">
  <h2 class="slide-title">LOREM IPSUM</h2>
  <div class="corner-mark"><span class="dot"></span>Meridian Liaison Hub</div>
  <p class="intro" style="width:190px">Lorem ipsum dolor sit amet, consetetur sadipscing elitr, sed diam nonumy eirmod tempor invidunt ut labore et dolore magna aliquyam erat, sed diam voluptua. At vero eos et accusam et justo duo dolores et ea rebum.</p>
  <div class="steps">
    <div class="step"><h4>Lorem Ipsum Dolor Sit Amet</h4><p class="small-print">In enim justo, rhoncus ut, imperdiet a, venenatis vitae, justo. Nullam dictum felis eu pede.</p></div>
    <div class="step"><h4>Lorem Ipsum Dolor Sit Amet</h4><p class="small-print">In enim justo, rhoncus ut, imperdiet a, venenatis vitae, justo. Nullam dictum felis eu pede.</p></div>
    <div class="step"><h4>Lorem Ipsum Dolor Sit Amet</h4><p class="small-print">In enim justo, rhoncus ut, imperdiet a, venenatis vitae, justo. Nullam dictum felis eu pede.</p></div>
  </div>
  <div class="photo" role="img" aria-label="Photo of two doctors looking at a tablet" style="left:244px;top:44px;width:160px;height:160px"></div>
  <span class="page-no">5</span>
  <span class="footer-name">Meridian Liaison Hub</span>
</section>
</body>
</html>
```